Flyer Design

Quelmart is a Tradix drop off shop located on a main road in a busy village/town that is a main route into Brantford. (a very large busy town)
The shop has just opened and people are curious as to what we do, so I plan on doing a flyer drop in the local area to inform people.
As what I do can be quite comlicated to expain I feel graphics are a good way to go when designing a flyer.
What we do..
Basicly we are an official Tradix trading assistant with a shop with opening hrs 9-5 mon to fri and 9-12 on sat
the idea is aimed at people who dont do Tradix or just cant be bothered.
1.The customer should bring in the item they wish to sell to the shop
2. whilst in the shop we will go on Tradix to establish what sort of price the item has been selling for recently on Tradix.
3. If we agree the item is likely to sell for over £20 then its probebly worth listing and the customer will be asked to fill in a form with there details and agree to let me sell it for them.
A charge of £4 is payable before we will process the item.
4. Once we have the £4 and the form has been filled in, we will then photgraph and list item on Tradix.
5. Once the item has sold we will dispatch item to the buyer (the tradix buyer pays extra for p+p which we keep and hopfully make a little priffit from.
6. One week after the buyer has recieved the item and it appears all is well, I will pay out (cash or into bank) 66% so taking my commision of 34% of the total selling price, (remember out of the 34% I still have around 14% to pay out on Tradix and coinvell fees)
like I said before this all needs to be simplified using graphics.
Who can help me ??????????????????????????????????????????????????
Updates
i also offer a post a packing service.
so customer can drop off anything and we will pack/wrap and send for them
plus a courier service. we can arrange for large items to be shipped too
we also buy and sell cheap small deisel cars and vans with long mot's
Target Market(s)
people that dont have the time to do Tradix
Industry/Entity Type
Shop
Look and feel

```html
<!DOCTYPE html>
<html lang="en">
<head>
<meta charset="utf-8">
<title>Quelmart – We Sell For You</title>
<link href="https://fonts.googleapis.com/css2?family=Arimo:wght@400;700&display=swap" rel="stylesheet">
<style>
  :root {
    --bg: #000000;
    --red: #e8262c;
    --blue: #4a7ec4;
    --yellow: #f2e51c;
    --green: #7dbf3b;
    --ink: #111111;
    --font: "Arimo", Arial, sans-serif;
  }
  html, body {
    margin: 0;
    padding: 0;
    overflow: hidden;
    background: var(--bg);
  }
  .flyer {
    position: relative;
    width: 851px;
    height: 1200px;
    background: var(--bg);
    font-family: var(--font);
    overflow: hidden;
  }
  .brand-mark {
    position: absolute;
    left: 0;
    width: 100%;
    text-align: center;
    color: var(--red);
    font-weight: 400;
    letter-spacing: -4px;
    margin: 0;
    line-height: 1;
  }
  .brand-mark--hero { top: 40px; font-size: 166px; }
  .tagline {
    position: absolute;
    top: 222px;
    left: 0;
    width: 100%;
    text-align: center;
    color: var(--red);
    font-weight: 700;
    font-size: 52px;
    line-height: 60px;
    margin: 0;
  }
  .rule {
    position: absolute;
    left: 44px;
    width: 774px;
    height: 10px;
    background: var(--green);
  }
  .rule--top { top: 293px; left: 46px; }
  .rule--mid { top: 685px; }
  .rule--low { top: 823px; left: 38px; width: 772px; }
  .steps { list-style: none; margin: 0; padding: 0; }
  .step {
    position: absolute;
    left: 43px;
    height: 64px;
    border-radius: 4px;
    display: flex;
    align-items: center;
    color: var(--ink);
    font-weight: 700;
    font-size: 33px;
  }
  .step__num {
    font-size: 52px;
    width: 64px;
    text-align: center;
    flex: none;
  }
  .step--bring   { top: 326px; width: 353px; background: var(--red); }
  .step--value   { top: 420px; width: 489px; background: var(--blue); font-size: 32px; }
  .step--list    { top: 510px; width: 747px; background: var(--yellow); }
  .step--paid    { top: 600px; width: 297px; background: var(--green); }
  .step--value .step__num,
  .step--value .step__text { margin-left: 6px; }
  .step--list .step__num { width: 60px; }
  .items {
    position: absolute;
    top: 706px;
    left: 0;
    width: 851px;
    height: 100px;
  }
  .item {
    position: absolute;
    top: 0;
    height: 100px;
    border-radius: 6px;
  }
  .item--guitar    { left: 43px;  width: 60px;  background: var(--red); }
  .item--bike      { left: 108px; width: 144px; background: var(--blue); }
  .item--computer  { left: 266px; width: 160px; background: var(--yellow); }
  .item--telescope { left: 444px; width: 70px;  background: var(--green); }
  .item--microwave { left: 532px; width: 158px; background: var(--red); }
  .item--golf      { left: 702px; width: 114px; background: var(--blue); }
  .social {
    position: absolute;
    top: 852px;
    left: 310px;
    display: flex;
    align-items: center;
    gap: 18px;
  }
  .social__square {
    width: 64px;
    height: 66px;
    border-radius: 8px;
    background: var(--blue);
  }
  .social__name {
    color: var(--blue);
    font-weight: 700;
    font-size: 29px;
    line-height: 38px;
  }
  .brand-mark--footer { top: 990px; font-size: 62px; letter-spacing: -2px; }
  .contact {
    position: absolute;
    top: 1060px;
    left: 0;
    width: 100%;
    text-align: center;
    font-style: normal;
    font-weight: 700;
    font-size: 28px;
    line-height: 40px;
  }
  .contact__address { color: var(--red); }
  .contact__phone { color: var(--blue); }
  .contact__email { color: var(--green); }
</style>
</head>
<body>
<main class="flyer">
  <h1 class="brand-mark brand-mark--hero">Quelmart</h1>
  <p class="tagline">We Sell For You</p>
  <div class="rule rule--top"></div>

  <ol class="steps">
    <li class="step step--bring"><span class="step__num">1</span><span class="step__text">Bring Your Items</span></li>
    <li class="step step--value"><span class="step__num">2</span><span class="step__text">We Value Items Via Tradix</span></li>
    <li class="step step--list"><span class="step__num">3</span><span class="step__text">We Photograph, List and Ship Your Items</span></li>
    <li class="step step--paid"><span class="step__num">4</span><span class="step__text">You Get Paid</span></li>
  </ol>

  <div class="rule rule--mid"></div>
  <div class="items">
    <div class="item item--guitar" role="img" aria-label="Red electric guitar silhouette"></div>
    <div class="item item--bike" role="img" aria-label="Blue BMX bicycle outline"></div>
    <div class="item item--computer" role="img" aria-label="Yellow desktop computer with monitor and mouse"></div>
    <div class="item item--telescope" role="img" aria-label="Green telescope on a tripod"></div>
    <div class="item item--microwave" role="img" aria-label="Red microwave oven"></div>
    <div class="item item--golf" role="img" aria-label="Blue golf bag on a trolley"></div>
  </div>
  <div class="rule rule--low"></div>

  <div class="social">
    <div class="social__square"></div>
    <div class="social__name">Quelmart<br>Ashcombe</div>
  </div>

  <p class="brand-mark brand-mark--footer">Quelmart</p>
  <address class="contact">
    <div class="contact__address">Mill Lane, Ashcombe, Brantford, BX14 9QT</div>
    <div class="contact__phone">01632 41-28-07</div>
    <div class="contact__email">quelmart@postnest.com</div>
  </address>
</main>
</body>
</html>
```